Flyer-Design für Wäscherei sucht Design
Zielgruppe
Wir sind eine Wäscherei.
Zielgruppe: Kunden aus der Hotel- und Gastronomiebranche
Aufgabenstellung
Wir benötigen einen 2-seitigen Flyer DIN lang. 9,8 x21cm
TextInhalte sind in der Vorlage-Datei.
Bilder sind eingefügt.

```html
<!DOCTYPE html>
<html lang="de">
<head>
<meta charset="utf-8">
<title>Serviettenfaltservice – Wäscherei Lindholm</title>
<link href="https://fonts.googleapis.com/css2?family=Open+Sans:wght@400;700&family=Great+Vibes&display=swap" rel="stylesheet">
<style>
  :root {
    --ink: #1a1a1a;
    --magenta: #f01ee0;
    --paper: #ffffff;
    --footer-line: #dcdcdc;
    --footer-veil: #f3f3f3;
  }
  * { margin: 0; padding: 0; box-sizing: border-box; }
  html, body { width: 1200px; height: 560px; overflow: hidden; background: var(--paper); }
  .flyer {
    position: relative; width: 1200px; height: 560px; overflow: hidden;
    font-family: "Open Sans", Arial, sans-serif; color: var(--ink);
  }
  .intro {
    position: absolute; left: 57px; top: 46px; width: 800px;
    font-size: 17.4px; line-height: 24.2px; letter-spacing: -0.1px;
  }
  .service-title {
    position: absolute; left: 44px; top: 148px;
    font-family: "Great Vibes", cursive; font-weight: 400;
    font-size: 74px; line-height: 1; color: var(--magenta);
  }
  .price-list {
    position: absolute; left: 57px; top: 273px; width: 789px;
    font-size: 18.4px; line-height: 24.2px;
  }
  .price-row { display: flex; }
  .price-row .category { width: 250px; }
  .price-row .forms { font-weight: 700; flex: 1; }
  .price-row .price { text-align: right; }
  .vat-note {
    position: absolute; right: 355px; top: 332px;
    font-size: 14px;
  }
  .closing {
    position: absolute; left: 57px; top: 410px; width: 800px;
    font-size: 18.4px; line-height: 24.2px;
  }
  .footer {
    position: absolute; left: 0; top: 490px; width: 1200px; height: 70px;
    border-top: 1px solid var(--footer-line);
  }
  .contact {
    position: absolute; left: 57px; top: 25px;
    font-size: 14px; letter-spacing: 0.2px;
  }
  .photo {
    position: absolute; left: 865px; top: 0; width: 335px; height: 560px;
    background:
      linear-gradient(180deg, rgba(160,40,20,0.85) 0%, rgba(40,20,20,0.9) 22%, rgba(30,25,25,0.6) 40%, rgba(235,235,235,0) 60%),
      linear-gradient(100deg, #c02a1a 0%, #e8e8e8 45%, #f7f7f7 100%);
  }
  .photo-veil {
    position: absolute; left: 865px; top: 490px; width: 335px; height: 70px;
    background: var(--footer-veil); opacity: 0.92;
  }
  .brand {
    position: absolute; left: 940px; top: 513px;
    font-size: 15px; font-weight: 700; color: var(--magenta); letter-spacing: 0.3px;
  }
</style>
</head>
<body>
<div class="flyer">
  <p class="intro">Wir optimieren Ihren Serviettenfaltprozess. Wir entlasten Sie von dieser demotivierenden und unproduktiven Tätigkeit. Wir falten Ihnen Ihre Stoffservietten oder unsere Mietservietten vor. Hygienisch, zuverlässig und wirtschaftlich – bereit für die Mise en Place.</p>

  <h1 class="service-title">Serviettenfaltservice</h1>

  <div class="price-list">
    <div class="price-row"><span class="category">Faltformen Kategorie 1:</span><span class="forms">Welle, Kerze, Fächer</span><span class="price">je Faltung für nur 0,20 € *</span></div>
    <div class="price-row"><span class="category">Faltformen Kategorie 2:</span><span class="forms">Pyramide, Bischofsmütze</span><span class="price">je Faltung für nur 0,35 € *</span></div>
  </div>
  <p class="vat-note">*zzgl. gesetzliche MwSt.</p>

  <p class="closing">Weitere Formen sind auf Anfrage möglich. Bei Bedarf stellen wir Ihnen Mietservietten für nur 0,25 €* je Stück zur Verfügung. Mindestabnahmemenge: 100 Stück</p>

  <div class="photo" role="img" aria-label="Gedeckter Restauranttisch mit gefalteter weißer Stoffserviette, Weingläsern und roter Rose"></div>

  <footer class="footer">
    <p class="contact">Wäscherei Lindholm • Gartenweg 12 • 70999 Talheim • Tel. +49 (0) 7000 / 12 34 56 • info@waescherei-lindholm.de</p>
  </footer>
  <div class="photo-veil"></div>
  <div class="brand">WÄSCHEREI LINDHOLM</div>
</div>
</body>
</html>
```